Farhan Jewellers Stationary Contest

Pakistan’s largest Jewellery, Diamond and luxury watches store requires professional stationery. We have a long list of are trusted clients since 1959, our third generation has successfully maintained and sustained the legacy and excellence in the sector.

We require stationery template as part of this contest. The stationery can be double sided.

We prefer a design that makes use of some of the premium business stationery printing options, such as foil stamping, embossing/debossing, painted edges, spot UV etc (doesn't have to use all these options, only what you feel works, but we are looking for a design that stands out and is memorable and these nice touches have that effect.)

We want an eye catching, innovative, high end professional looking stationery for an out of box design that blends well with our new logo (attached). We want the design to be an out of box solution, you may use any element to compliment the logo. You may consider incorporating watermark etc, highlighting our products (Gold and Diamond Jewellery in addition to Luxury watches)

Company details are as follows;

Company name: Farhan Jewellers
Contact Person: Tariq Naveed
Designation: Business Development Consultant
Mobile: +92 333 815 6042
Email: tariqnaveed@mailvora.com
Website: www.farhanjewellers-pk.net

Target Market(s)

Matrimonial, Elite & Businesses class, Upmarket

Font styles to use
Other font styles liked:
• Designers choice

Colors

Designer to choose colors to be used in the design.

Requirements
Must have
• Look and feel: Upmarket, innovative, Modern, Professional, graceful, Elegant, designer stuff.
Nice to have
• Unique design

```html
<!DOCTYPE html>
<html lang="en">
<head>
<meta charset="utf-8">
<title>Farhan Jewellers – Business Card</title>
<link rel="stylesheet" href="https://fonts.googleapis.com/css2?family=Montserrat:wght@500;600;700&display=swap">
<style>
  :root {
    --backdrop: #35302c;
    --card: #1d1e21;
    --gold: #e2a530;
    --gold-edge: #b8923f;
    --ink-light: #f2f0ec;
  }
  html, body {
    margin: 0;
    padding: 0;
    width: 1200px;
    height: 769px;
    overflow: hidden;
    background: var(--backdrop);
    font-family: "Montserrat", Arial, sans-serif;
  }
  .canvas {
    position: relative;
    width: 1200px;
    height: 769px;
  }
  .card {
    position: absolute;
    background: var(--card);
    box-shadow: 0 0 0 3px var(--gold-edge), 0 18px 40px rgba(0,0,0,.45);
    box-sizing: border-box;
  }

  /* Front: portrait contact side */
  .card-front {
    left: 130px;
    top: 100px;
    width: 340px;
    height: 570px;
    display: flex;
    flex-direction: column;
    align-items: center;
    padding-top: 62px;
    text-align: center;
  }
  .brand-lockup {
    display: flex;
    align-items: center;
    gap: 12px;
  }
  .brand-dot {
    width: 26px;
    height: 26px;
    border-radius: 50%;
    background: var(--gold);
  }
  .brand-name {
    color: var(--gold);
    font-weight: 600;
    font-size: 25px;
    letter-spacing: 1px;
    text-transform: uppercase;
    line-height: 1.05;
    text-align: left;
  }
  .company-line {
    margin-top: 26px;
    color: var(--gold);
    font-weight: 700;
    font-size: 15px;
    letter-spacing: .5px;
    text-transform: uppercase;
  }
  .person-name {
    margin-top: 46px;
    color: var(--gold);
    font-weight: 600;
    font-size: 19px;
    text-transform: uppercase;
  }
  .person-title {
    margin-top: 6px;
    color: var(--ink-light);
    font-weight: 600;
    font-size: 13px;
    line-height: 1.35;
    text-transform: uppercase;
  }
  .divider {
    width: 16px;
    height: 1px;
    background: var(--ink-light);
    margin: 20px 0;
  }
  .contact-line {
    color: var(--ink-light);
    font-weight: 600;
    font-size: 14px;
    line-height: 1.5;
  }
  .contact-line.email {
    font-size: 12px;
    text-transform: uppercase;
  }
  .website-line {
    color: var(--gold);
    font-weight: 600;
    font-size: 15px;
    text-transform: uppercase;
    margin-top: 2px;
  }

  /* Back: landscape brand side */
  .card-back {
    left: 560px;
    top: 200px;
    width: 540px;
    height: 320px;
    display: flex;
    flex-direction: column;
    align-items: center;
    justify-content: center;
  }
  .card-back .brand-lockup { gap: 16px; }
  .card-back .brand-dot { width: 34px; height: 34px; }
  .card-back .brand-name { font-size: 34px; }
  .back-website {
    margin-top: 44px;
    color: var(--ink-light);
    font-weight: 600;
    font-size: 12px;
    letter-spacing: 4px;
    text-transform: uppercase;
  }
</style>
</head>
<body>
<main class="canvas">
  <section class="card card-front" aria-label="Business card front">
    <div class="brand-lockup">
      <span class="brand-dot"></span>
      <span class="brand-name">Farhan<br>Jewellers</span>
    </div>
    <div class="company-line">Farhan Jewellers</div>
    <div class="person-name">Tariq Naveed</div>
    <div class="person-title">Business Development<br>Consultant</div>
    <div class="divider"></div>
    <div class="contact-line">+92 333 815 6042</div>
    <div class="contact-line email">tariqnaveed@mailvora.com</div>
    <div class="divider"></div>
    <div class="website-line">farhanjewellers-pk.net</div>
  </section>

  <section class="card card-back" aria-label="Business card back">
    <div class="brand-lockup">
      <span class="brand-dot"></span>
      <span class="brand-name">Farhan Jewellers</span>
    </div>
    <div class="back-website">www.farhanjewellers-pk.net</div>
  </section>
</main>
</body>
</html>
```